Webinar Series Announcement Flyer for Non-profit

We need a flyer design for a non-profit organization based in Washington, DC called "VELTRO, The Guild for Recovery Practitioners". VELTRO, the Guild for Recovery Practitioners, represents the professional interests of more than 75,000 addiction counselors, educators and other addiction-focused health care professionals in the United States, Canada and abroad. VELTRO’s members are addiction counselors, educators and other addiction-focused health care professionals, who specialize in addiction prevention, treatment, recovery support and education. An important part of the healthcare continuum, VELTRO members and its 44 state affiliates work to create healthier individuals, families and communities through prevention, intervention, quality treatment and recovery support.

We are co-hosting an 8 event webinar series in 2014 and need a flyer to present the critical information in a PDF.

All companies involved must have their logos and names on the flyer:
• The KEW Project
• National MOLDEP RHCX
• PLEV at the Harmon Ridge Institute
• VELTRO, The Guild for Recovery Practitioners

The purpose of the flyer is to promote and recruit potential participants to the live events.

We would like to see designs that use blue, the main color of our website (http://wardmoldep.sitecraft-example.com/).

The final design should communicate professionalism, education and free and there is a great benefit to the individual for participating in the webinar series.

Target Market(s)

Our membership potentials are professionals, mostly women and a few men, aged 23 to 65 who are all trained as therapists and care about people.

Industry/Entity Type

Non Profit

Requirements
Must have
• The flyer must be one page.
• It must be easy to read.
• Must have graphics and attractive color - if a group of people, must be culturally diverse.
• Must contain all four logos - three are clumped together and one is separate.
• Must be clean and modern/contemporary in tone.
• Must include the text that is in the attached Word document - FYI, there will be minor wording changes to the document prior to finalization but the basic structure and elements should still remain the same.

```html
<!DOCTYPE html>
<html lang="en">
<head>
<meta charset="utf-8">
<title>MOLDEP Webinar Series 2014</title>
<link href="https://fonts.googleapis.com/css2?family=Open+Sans:wght@400;600;700;800&family=Arimo:wght@400;700&display=swap" rel="stylesheet">
<style>
  :root {
    --navy: #26355c;
    --steel: #8b8e93;
    --band-gray: #c9cbce;
    --sched-top: #9fa2a7;
    --sched-bottom: #c8cacd;
    --ink: #1e1e1e;
    --white: #ffffff;
  }
  * { box-sizing: border-box; margin: 0; padding: 0; }
  html, body { width: 873px; height: 1200px; overflow: hidden; background: var(--white); }
  body { position: relative; font-family: "Arimo", Arial, sans-serif; color: var(--ink); }

  .masthead {
    position: absolute; left: 0; top: 0; width: 873px; height: 158px;
    background: var(--navy);
    border-bottom: 10px solid var(--band-gray);
  }
  .masthead__title {
    position: absolute; left: 0; right: 0; top: 42px; text-align: center;
    font-family: "Open Sans", Arial, sans-serif; font-weight: 800;
    font-size: 76px; line-height: 1; letter-spacing: -1px; white-space: nowrap;
  }
  .masthead__acronym { color: var(--white); }
  .masthead__word { color: var(--steel); }
  .masthead__series {
    position: absolute; right: 120px; top: 22px;
    font-family: "Open Sans", Arial, sans-serif; font-weight: 700;
    font-size: 25px; letter-spacing: 5px; color: var(--white);
  }

  .intro { position: absolute; left: 38px; top: 184px; width: 800px; }
  .intro__partners { font-size: 17px; line-height: 1.3; margin-bottom: 12px; }
  .benefits { list-style: disc; padding-left: 50px; font-size: 16.5px; line-height: 21px; }
  .benefits li { padding-left: 8px; max-width: 620px; }
  .benefits li.short { max-width: 560px; }

  .ce-callout {
    position: absolute; left: 680px; top: 246px; width: 193px; height: 108px;
    background: var(--navy); color: var(--white);
    border-radius: 12px 0 0 12px;
    padding: 13px 14px 0 20px; font-size: 17px; line-height: 1.25;
  }
  .ce-callout strong { font-weight: 700; }

  .schedule-head { position: absolute; left: 0; top: 614px; width: 873px; height: 46px; }
  .schedule-head__text {
    position: absolute; left: 22px; top: 7px;
    font-family: "Open Sans", Arial, sans-serif; font-weight: 700;
    font-size: 25px; color: var(--white);
  }
  .schedule {
    position: absolute; left: 0; top: 660px; width: 873px; height: 306px;
    background: linear-gradient(180deg, var(--sched-top), var(--sched-bottom));
    border-bottom: 3px solid var(--navy);
    padding: 14px 20px 0 30px;
    display: grid; grid-template-columns: 430px 1fr;
  }
  .schedule__col { display: flex; flex-direction: column; gap: 10px; }
  .event { display: grid; grid-template-columns: 86px 1fr; font-size: 15.5px; line-height: 19px; }
  .event__date { font-weight: 700; color: var(--navy); }
  .event__title { color: var(--ink); max-width: 300px; }

  .partners {
    position: absolute; left: 0; top: 972px; width: 873px; height: 160px;
    display: flex; align-items: center; justify-content: space-between;
    padding: 0 26px 0 40px;
  }
  .partner { display: flex; align-items: center; gap: 10px; color: var(--navy);
    font-weight: 700; font-size: 17px; line-height: 1.15; }
  .partner__mark { width: 18px; height: 18px; background: var(--navy); flex: none; }
  .partner__mark--round { border-radius: 50%; }
  .partner--lead { border: 3px solid var(--navy); padding: 14px 16px; font-size: 22px; }

  .footer {
    position: absolute; left: 0; top: 1134px; width: 873px; height: 66px;
    background: var(--navy);
  }
  .footer__text {
    position: absolute; left: 0; right: 0; top: 50%; transform: translateY(-50%);
    text-align: center; white-space: nowrap; color: var(--white);
    font-family: "Open Sans", Arial, sans-serif; font-size: 17px; line-height: 1;
  }
  .footer__text strong { font-weight: 700; }
</style>
</head>
<body>
  <header class="masthead">
    <div class="masthead__series">SERIES</div>
    <h1 class="masthead__title"><span class="masthead__acronym">MOLDEP</span> <span class="masthead__word">webinar</span></h1>
  </header>

  <section class="intro">
    <p class="intro__partners">Produced in partnership with The KEW Project, National MOLDEP RHCX, PLEV at the Harmon Ridge Institute and VELTRO, The Guild for Recovery Practitioners</p>
    <ul class="benefits">
      <li>Free live events held monthly</li>
      <li>Free 24/7 on-demand viewing</li>
      <li>Free CEs for everyone</li>
      <li>Only 1.5 hours of your day</li>
      <li>New topics premiere each month</li>
      <li>Participate from work, home, or on the go!</li>
      <li>Renew your professional license/certification</li>
      <li class="short">Only need a computer/internet connection or a smartphone (compatible with desktop, laptop, tablet, phone)</li>
      <li>Expert presenters from across the country</li>
      <li>Ideal for addiction professionals, medical professionals, nurses, social workers, mental health counselors, professional counselors, psychologists, employee assistance professionals, and other helping professionals that are interested in learning about MOLDEP</li>
      <li>Watch together and use as a component of clinical supervision or watch with your colleagues</li>
    </ul>
  </section>

  <aside class="ce-callout">Get 12 <strong>free</strong> CEs through this collaborative webinar series</aside>

  <div class="schedule-head">
    <svg width="873" height="46" viewBox="0 0 873 46" aria-hidden="true">
      <polygon points="0,0 415,0 390,46 0,46" fill="var(--navy)"/>
      <rect x="0" y="43" width="873" height="3" fill="var(--navy)"/>
    </svg>
    <h2 class="schedule-head__text">2014 Upcoming Schedule</h2>
  </div>

  <section class="schedule">
    <div class="schedule__col">
      <div class="event"><span class="event__date">Jan 29</span><span class="event__title">MOLDEP and Health Reform – Presented by Priya Ramanath, Owen Hartley and Gil Marston</span></div>
      <div class="event"><span class="event__date">Feb 19</span><span class="event__title">Overview of MOLDEP: A Nursing Response to the Full Spectrum of Substance Use – Presented by Dana Felwick and Laura Brennick</span></div>
      <div class="event"><span class="event__date">Mar 12</span><span class="event__title">MOLDEP in the Criminal Justice System – Presented by Andrea Ellory and Alina Kossar</span></div>
      <div class="event"><span class="event__date">Apr 9</span><span class="event__title">Reducing Opioid Risk with MOLDEP – Presented by Anne Balston</span></div>
    </div>
    <div class="schedule__col">
      <div class="event"><span class="event__date">May 14</span><span class="event__title">Treatment of Tobacco Dependence in the Healthcare Setting: Current Best Practices – Presented by Brent Callister</span></div>
      <div class="event"><span class="event__date">Jun 11</span><span class="event__title">Applying MOLDEP to Depression, Prescription Medication Abuse, Tobacco Use, Trauma &amp; Other Concerns – Presented by Reid Barlow</span></div>
      <div class="event"><span class="event__date">Jul 9</span><span class="event__title">Training Integrated Behavioral Health in Social Work – Presented by Joel Castellano</span></div>
      <div class="event"><span class="event__date">Aug 6</span><span class="event__title">Why Integrative Care? – Presented by Ben Mayhurst</span></div>
    </div>
  </section>

  <section class="partners">
    <div class="partner"><span class="partner__mark partner__mark--round"></span><span>PLEV at the<br>Harmon Ridge Institute</span></div>
    <div class="partner"><span class="partner__mark"></span><span>The KEW<br>Project</span></div>
    <div class="partner"><span class="partner__mark partner__mark--round"></span><span>National<br>MOLDEP RHCX</span></div>
    <div class="partner partner--lead"><span>VELTRO</span></div>
  </section>

  <footer class="footer">
    <p class="footer__text">Please visit <strong>wardmoldep.sitecraft-example.com/webinars</strong> for more information and to register</p>
  </footer>
</body>
</html>
```